Stylish Business Cards Wanted

- DOUBLE SIDED Design Required -

High end, edgy cards for a corporate and personal stylist. Must include logo,
Name: Belinda Marsh
Title: Director and Stylist
telephone : +61 8 8417 2950
email: belinda@thewardrobeledger.com
website: thewardrobeledger.com
Tag: Corporate Workwear & Uniform Specialist | Personal Stylist
Would like nice icons for telephone, email, website

Target Market(s)

Businesses wanting stylish uniforms, people wanting stylish wardrobes

Industry/Entity Type

Corporate Workwear Stylist

Contact Information for Business Card

I would like black, white and gold foiling incorporated in the design - possibly a touch of the other colours on my branding guide attached Name: Belinda Marsh Title: Director and Stylist telephone : +61 8 8417 2950 email: belinda@thewardrobeledger.com website: thewardrobeledger.com Tag: Corporate Workwear & Uniform Specialist | Personal Stylist Would like nice icons for telephone, email, website

Font styles to use
Other font styles liked:
• Raleway

Colors

Designer to choose colors to be used in the design.

Requirements
Must have
• Gold foil accents

```html
<!DOCTYPE html>
<html lang="en">
<head>
<meta charset="utf-8">
<title>The Wardrobe Ledger – Business Cards</title>
<link rel="stylesheet" href="https://fonts.googleapis.com/css2?family=Montserrat:wght@400;500;700&display=swap">
<style>
  :root {
    --backdrop: #2e2e2e;
    --card: #232323;
    --card-deco: #1c1c1c;
    --gold: #e6b843;
    --white: #ffffff;
    --text-font: "Montserrat", Arial, sans-serif;
  }
  * { box-sizing: border-box; margin: 0; padding: 0; }
  html, body { width: 1200px; height: 900px; overflow: hidden; background: var(--backdrop); }
  .canvas {
    width: 1200px; height: 900px;
    display: flex; flex-direction: column; align-items: center; justify-content: center; gap: 40px;
    font-family: var(--text-font);
  }
  .card {
    position: relative;
    width: 640px; height: 388px;
    background: var(--card);
    border-left: 4px solid var(--gold);
    border-bottom: 4px solid var(--gold);
    box-shadow: 0 14px 30px rgba(0,0,0,.45);
    overflow: hidden;
  }

  /* Brand name block */
  .brand { display: flex; align-items: center; gap: 12px; color: var(--white); font-weight: 700; }
  .brand-mark { width: 14px; height: 14px; background: var(--gold); flex: none; }
  .brand-name { text-transform: uppercase; letter-spacing: .16em; }

  /* Front */
  .card-front .brand { position: absolute; left: 0; right: 0; top: 140px; justify-content: center; }
  .card-front .brand-name { font-size: 30px; }
  .tagline {
    position: absolute; left: 0; right: 0; bottom: 40px; text-align: center;
    color: var(--gold); font-size: 14px; font-weight: 500; letter-spacing: .06em;
  }

  /* Back */
  .card-back .brand { position: absolute; left: 50px; top: 54px; }
  .card-back .brand-name { font-size: 22px; }
  .deco {
    position: absolute; right: 30px; top: 40px; width: 190px; height: 300px;
    background: var(--card-deco); border-radius: 90px 90px 20px 20px;
  }
  .person { position: absolute; left: 50px; top: 168px; }
  .person-name { color: var(--gold); font-size: 26px; font-weight: 700; letter-spacing: .04em; text-transform: uppercase; }
  .person-title { color: var(--white); font-size: 16px; font-weight: 400; margin-top: 2px; }
  .contacts { position: absolute; left: 50px; top: 256px; list-style: none; }
  .contacts li { display: flex; align-items: center; gap: 12px; color: var(--white); font-size: 16px; line-height: 32px; }
  .contacts svg { width: 18px; height: 18px; fill: var(--gold); flex: none; }
</style>
</head>
<body>
<main class="canvas">

  <section class="card card-front" aria-label="Business card front">
    <div class="brand">
      <span class="brand-mark"></span>
      <span class="brand-name">The Wardrobe Ledger</span>
    </div>
    <p class="tagline">Corporate Workwear &amp; Uniform Specialist | Personal Stylist</p>
  </section>

  <section class="card card-back" aria-label="Business card back">
    <div class="deco" role="img" aria-label="Faint oversized script lettering decoration"></div>
    <div class="brand">
      <span class="brand-mark"></span>
      <span class="brand-name">The Wardrobe Ledger</span>
    </div>
    <div class="person">
      <h1 class="person-name">Belinda Marsh</h1>
      <p class="person-title">Director and Stylist</p>
    </div>
    <ul class="contacts">
      <li>
        <svg viewBox="0 0 24 24" aria-hidden="true"><path d="M6.6 10.8a15.1 15.1 0 0 0 6.6 6.6l2.2-2.2c.3-.3.7-.4 1-.2 1.1.4 2.3.6 3.6.6.6 0 1 .4 1 1V20c0 .6-.4 1-1 1A17 17 0 0 1 3 4c0-.6.4-1 1-1h3.5c.6 0 1 .4 1 1 0 1.3.2 2.5.6 3.6.1.3 0 .7-.2 1z"/></svg>
        +61 8 8417 2950
      </li>
      <li>
        <svg viewBox="0 0 24 24" aria-hidden="true"><path d="M2 5h20v14H2zm2 2v.5l8 5 8-5V7zm0 2.8V17h16V9.8l-8 5z"/></svg>
        belinda@thewardrobeledger.com
      </li>
      <li>
        <svg viewBox="0 0 24 24" aria-hidden="true"><path d="M12 2a10 10 0 1 0 0 20 10 10 0 0 0 0-20zm6.9 6h-3a15 15 0 0 0-1.3-3.9A8 8 0 0 1 18.9 8zM12 4c.8 1.2 1.5 2.5 1.9 4h-3.8c.4-1.5 1.1-2.8 1.9-4zM4.3 14a8 8 0 0 1 0-4h3.4a16 16 0 0 0 0 4zm.8 2h3a15 15 0 0 0 1.3 3.9A8 8 0 0 1 5.1 16zm3-8h-3a8 8 0 0 1 4.3-3.9C8.8 5.3 8.4 6.6 8.1 8zM12 20c-.8-1.2-1.5-2.5-1.9-4h3.8c-.4 1.5-1.1 2.8-1.9 4zm2.3-6H9.7a14 14 0 0 1 0-4h4.6a14 14 0 0 1 0 4zm.3 5.9c.6-1.2 1-2.5 1.3-3.9h3a8 8 0 0 1-4.3 3.9zm1.7-5.9a16 16 0 0 0 0-4h3.4a8 8 0 0 1 0 4z"/></svg>
        www.thewardrobeledger.com
      </li>
    </ul>
  </section>

</main>
</body>
</html>
```